Visitenkarten-Design für Steuerberater und Wirtschaftsprüfer
Zielgruppe
Steuerberater, Wirtschaftsprüfer in München
Aufgabenstellung
Wir haben ein Logo das uns gefällt, jetzt allerdings steht die Umfirmierung vor der Tür und aus der Kanzlei Seidelt (so unser Name) wird Seidelt und Partner mbB (die Jugend kommt mit als Partner in die Kanzlei) , Steuerberater, Wirtschaftsprüfer
Analog unseres alten Briefpapiers und der alten Visitenkarten soll eigentlich nur der Zusatz 'und Partner mbB' oder '& Partner mbB' gestaltet werden.
Das Dateiformat bei Visitenkarten bitte so übergeben, dass wir Namen selbst austauschen mit gängigen Officeprogrammen austauschen können. Bei den Visitenkarten ist das große 'Seidelt' geprägt.
Ich stelle das Logo, das aktuelle Briefpapier und aktuelle Visitenkarten ein. Unsere Farbe ist grau.
Das Logo bitte in .pdf, .png, .psd und .eps (sagt mi alles nichts, haben wir aber alles schon mal irgendwo gebraucht) , Visiten karten auch in .pddf und .ai
Bei Fragen kontaktiert mich gern jederzeit.

```html
<!DOCTYPE html>
<html lang="de">
<head>
<meta charset="utf-8">
<title>Seidelt &amp; Partner mbB – Visitenkarten</title>
<link href="https://fonts.googleapis.com/css2?family=Questrial&display=swap" rel="stylesheet">
<style>
  :root {
    --page: #ffffff;
    --card: #5d5e60;
    --logo-front: #a3a1a2;
    --white: #ffffff;
    --muted: #c4c4c4;
    --rule: #d8d8d8;
  }
  * { box-sizing: border-box; margin: 0; padding: 0; }
  html, body { width: 1200px; height: 900px; overflow: hidden; background: var(--page); }
  body { position: relative; font-family: "Questrial", "Century Gothic", sans-serif; }

  .card {
    position: absolute;
    width: 508px; height: 290px;
    background: var(--card);
    box-shadow: 0 1px 3px rgba(0,0,0,.25);
  }
  .card--front-a { left: 36px;  top: 136px; }
  .card--front-b { left: 626px; top: 136px; }
  .card--back-a  { left: 38px;  top: 473px; }
  .card--back-b  { left: 629px; top: 473px; }

  /* Wortmarke Vorderseite */
  .brand { position: absolute; color: var(--logo-front); }
  .card--front-a .brand, .card--front-b .brand { left: 121px; top: 94px; width: 272px; }
  .brand__name { display: block; font-size: 62px; line-height: 1; letter-spacing: 4px; }
  .brand__suffix { display: block; font-size: 22px; line-height: 1.1; letter-spacing: 1px; margin-top: 2px; }
  .brand__rule { height: 1px; background: currentColor; margin-top: 3px; }
  .brand__tagline { display: block; font-size: 14.2px; letter-spacing: .6px; margin-top: 2px; white-space: nowrap; }

  /* Wortmarke Rückseite */
  .card--back-a .brand, .card--back-b .brand { right: 34px; top: 70px; width: 149px; color: var(--white); }
  .card--back-a .brand__name, .card--back-b .brand__name { font-size: 34px; letter-spacing: 2px; }
  .card--back-a .brand__suffix, .card--back-b .brand__suffix { font-size: 12px; letter-spacing: .5px; margin-top: 1px; }
  .card--back-a .brand__tagline, .card--back-b .brand__tagline { font-size: 7.8px; letter-spacing: .3px; margin-top: 2px; }

  .person { position: absolute; left: 36px; top: 64px; }
  .person__name { color: var(--white); font-size: 24px; line-height: 1; }
  .person__role { color: var(--muted); font-size: 10.5px; line-height: 12px; margin-top: 7px; }

  .divider { position: absolute; left: 36px; top: 200px; width: 440px; height: 1px; background: var(--rule); }

  .contact { position: absolute; top: 236px; display: flex; align-items: center; color: var(--white); }
  .contact__icon { width: 11px; height: 11px; fill: none; stroke: var(--white); stroke-width: 1.3; }
  .contact__bar { width: 1.5px; height: 14px; background: var(--white); margin: 0 7px 0 6px; }
  .contact__text { font-size: 10px; line-height: 11.5px; white-space: nowrap; }
  .contact--address { left: 25px; }
  .contact--phone   { left: 191px; }
  .contact--web     { left: 322px; top: 234px; }
</style>
</head>
<body>

  <section class="card card--front-a">
    <div class="brand">
      <span class="brand__name">SEIDELT</span>
      <span class="brand__suffix">&amp; PARTNER mbB</span>
      <span class="brand__tagline">STEUERBERATER | WIRTSCHAFTSPRÜFER</span>
    </div>
  </section>

  <section class="card card--front-b">
    <div class="brand">
      <span class="brand__name">SEIDELT</span>
      <span class="brand__suffix">&amp; PARTNER mbB</span>
      <div class="brand__rule"></div>
      <span class="brand__tagline">STEUERBERATER | WIRTSCHAFTSPRÜFER</span>
    </div>
  </section>

  <section class="card card--back-a">
    <div class="person">
      <p class="person__name">Lukas M. Seidelt</p>
      <p class="person__role">Dipl.-Kfm / Steuerberater<br>Wirtschaftsprüfer</p>
    </div>
    <div class="brand">
      <span class="brand__name">SEIDELT</span>
      <span class="brand__suffix">&amp; PARTNER mbB</span>
      <span class="brand__tagline">STEUERBERATER | WIRTSCHAFTSPRÜFER</span>
    </div>
    <div class="divider"></div>
    <div class="contact contact--address">
      <svg class="contact__icon" viewBox="0 0 12 12"><path d="M1 6.5 6 2l5 4.5M2.8 5.2V11h2.4V8h1.6v3h2.4V5.2" fill="var(--white)" stroke="none"/><path d="M1 6.5 6 2l5 4.5"/></svg>
      <span class="contact__bar"></span>
      <p class="contact__text">Lindenweg 12<br>80634 München</p>
    </div>
    <div class="contact contact--phone">
      <svg class="contact__icon" viewBox="0 0 12 12"><path d="M3 1.2 4.6 3.4 3.6 4.6c.6 1.5 1.9 2.9 3.5 3.6l1.1-1 2.2 1.6-1 1.7C6 10.3 1.7 6 1.4 2.2z"/></svg>
      <span class="contact__bar"></span>
      <p class="contact__text">T&nbsp; 089 - 47 21 3300<br>F 089 - 47 21 3309</p>
    </div>
    <div class="contact contact--web">
      <svg class="contact__icon" viewBox="0 0 12 12"><circle cx="6" cy="6" r="5"/><ellipse cx="6" cy="6" rx="2.2" ry="5"/><path d="M1 6h10M1.8 3.5h8.4M1.8 8.5h8.4"/></svg>
      <span class="contact__bar"></span>
      <p class="contact__text">info@kanzlei-seidelt.com<br>www.kanzlei-seidelt.com</p>
    </div>
  </section>

  <section class="card card--back-b">
    <div class="person">
      <p class="person__name">Lukas M. Seidelt</p>
      <p class="person__role">Dipl.-Kfm / Steuerberater<br>Wirtschaftsprüfer</p>
    </div>
    <div class="brand">
      <span class="brand__name">SEIDELT</span>
      <span class="brand__suffix">&amp; PARTNER mbB</span>
      <div class="brand__rule"></div>
      <span class="brand__tagline">STEUERBERATER | WIRTSCHAFTSPRÜFER</span>
    </div>
    <div class="divider"></div>
    <div class="contact contact--address">
      <svg class="contact__icon" viewBox="0 0 12 12"><path d="M1 6.5 6 2l5 4.5M2.8 5.2V11h2.4V8h1.6v3h2.4V5.2" fill="var(--white)" stroke="none"/><path d="M1 6.5 6 2l5 4.5"/></svg>
      <span class="contact__bar"></span>
      <p class="contact__text">Lindenweg 12<br>80634 München</p>
    </div>
    <div class="contact contact--phone">
      <svg class="contact__icon" viewBox="0 0 12 12"><path d="M3 1.2 4.6 3.4 3.6 4.6c.6 1.5 1.9 2.9 3.5 3.6l1.1-1 2.2 1.6-1 1.7C6 10.3 1.7 6 1.4 2.2z"/></svg>
      <span class="contact__bar"></span>
      <p class="contact__text">T&nbsp; 089 - 47 21 3300<br>F 089 - 47 21 3309</p>
    </div>
    <div class="contact contact--web">
      <svg class="contact__icon" viewBox="0 0 12 12"><circle cx="6" cy="6" r="5"/><ellipse cx="6" cy="6" rx="2.2" ry="5"/><path d="M1 6h10M1.8 3.5h8.4M1.8 8.5h8.4"/></svg>
      <span class="contact__bar"></span>
      <p class="contact__text">info@kanzlei-seidelt.com<br>www.kanzlei-seidelt.com</p>
    </div>
  </section>

</body>
</html>
```